Quarrow financial services, is a financial company that provides consultancy, brokerage services, and funding.

we will be providing the clients with insights, knowledge and data with regards to the financial markets.

with the brokerage services we will try to find the suitable counterparts that provide them with the best investments that suits their needs and expected return.

Target Market(s)

financial institutions, Corporates, high-net worth individuals

Industry/Entity Type

Financial Service

Contact Information for Business Card

Font styles to use
Other font styles liked:
• applemyungjo

Colors
00a990
848484

Requirements
Must have
• the logo at the back
Nice to have
• Finesse
Should not have
• boldness

```html
<!DOCTYPE html>
<html lang="en">
<head>
<meta charset="utf-8">
<title>Quarrow Financial Services – Business Card</title>
<link rel="stylesheet" href="https://fonts.googleapis.com/css2?family=Noto+Serif:wght@400&display=swap">
<style>
  :root {
    --teal: #00a990;
    --teal-line: #5cc4b3;
    --grey: #848484;
    --ink: #4a4f4e;
    --ink-on-teal: #4d5a57;
    --mark-tone: #c9d4c0;
    --paper: #ffffff;
    --backdrop: #ebe8e4;
  }
  * { margin: 0; padding: 0; box-sizing: border-box; }
  html, body {
    width: 1200px; height: 1000px; overflow: hidden;
    background: var(--backdrop);
    font-family: "Noto Serif", Georgia, serif;
    font-weight: 400;
  }
  .canvas { position: relative; width: 1200px; height: 1000px; }

  .card {
    position: absolute; left: 288px; width: 625px; height: 357px;
    border-radius: 24px;
    box-shadow: 0 6px 14px rgba(0,0,0,0.18);
  }
  .card--front { top: 140px; background: var(--teal); }
  .card--back { top: 532px; background: var(--paper); }

  /* Front brand lockup */
  .brand-front { position: absolute; left: 0; right: 0; top: 58px; text-align: center; color: var(--ink-on-teal); }
  .brand-front__square { width: 74px; height: 74px; margin: 0 auto 40px; background: var(--mark-tone); }
  .brand-front__name { font-size: 46px; letter-spacing: 2px; line-height: 1; text-transform: uppercase; }
  .brand-front__sub { font-size: 14px; letter-spacing: 2.5px; margin-top: 8px; text-transform: uppercase; }

  /* Back brand lockup */
  .brand-back { position: absolute; right: 36px; top: 38px; display: flex; align-items: center; gap: 12px; color: var(--ink); }
  .brand-back__square { width: 34px; height: 34px; background: var(--mark-tone); }
  .brand-back__name { font-size: 27px; letter-spacing: 1px; line-height: 1; text-transform: uppercase; }
  .brand-back__sub { font-size: 9.5px; letter-spacing: 1.6px; margin-top: 4px; text-transform: uppercase; text-align: center; }

  .person { position: absolute; left: 34px; top: 190px; }
  .person__name { color: var(--teal); font-size: 17px; letter-spacing: 0.5px; text-transform: uppercase; }
  .person__role { color: var(--ink); font-size: 13px; margin-top: 1px; }

  .divider { position: absolute; left: 34px; right: 36px; top: 241px; height: 1px; background: var(--teal-line); }

  .contacts { position: absolute; left: 34px; top: 258px; list-style: none; color: var(--ink); font-size: 13.5px; line-height: 20px; }
  .contacts li { display: flex; align-items: center; gap: 7px; }
  .contacts svg { width: 13px; height: 13px; fill: var(--teal); flex: none; }

  .address { position: absolute; right: 36px; top: 278px; text-align: right; color: var(--ink); font-size: 13.5px; line-height: 20px; }
</style>
</head>
<body>
<main class="canvas">
  <section class="card card--front" aria-label="Card front">
    <div class="brand-front">
      <div class="brand-front__square"></div>
      <div class="brand-front__name">Quarrow</div>
      <div class="brand-front__sub">Financial Services</div>
    </div>
  </section>

  <section class="card card--back" aria-label="Card back">
    <div class="brand-back">
      <div class="brand-back__square"></div>
      <div>
        <div class="brand-back__name">Quarrow</div>
        <div class="brand-back__sub">Financial Services</div>
      </div>
    </div>

    <div class="person">
      <div class="person__name">Daniel Hart</div>
      <div class="person__role">Founder &amp; CEO</div>
    </div>

    <div class="divider"></div>

    <ul class="contacts">
      <li>
        <svg viewBox="0 0 16 16" aria-hidden="true"><path d="M2 6c0-2 2-3 6-3s6 1 6 3v1h-3V5.5H5V7H2z"/><path d="M4 8h8l1.5 5h-11z"/></svg>
        012-555-0147
      </li>
      <li>
        <svg viewBox="0 0 16 16" aria-hidden="true"><path d="M1 3h14v10H1z M2.5 4.5 8 9l5.5-4.5" fill="none" stroke="#00a990" stroke-width="1.6"/><path d="M1 3h14L8 8.5z"/></svg>
        info@quarrowfinancial.com
      </li>
      <li>
        <svg viewBox="0 0 16 16" aria-hidden="true"><g fill="none" stroke="#00a990" stroke-width="1.3"><circle cx="8" cy="8" r="6.3"/><ellipse cx="8" cy="8" rx="2.8" ry="6.3"/><path d="M1.7 8h12.6M2.8 4.8h10.4M2.8 11.2h10.4"/></g></svg>
        www.quarrowfinancial.com
      </li>
    </ul>

    <address class="address" style="font-style:normal">
      Street name, Suite 100<br>
      State, Zip Code, Country
    </address>
  </section>
</main>
</body>
</html>
```